Disability and mental health support work company requires business card

Specialising
Wrenfield Disability is a new QCAP service aimed toward QCAP participants with a history of criminal justice, psychosocial/mental health, intellectual, and cognitive disabilities.

Our focus
Focusing on providing core QCAP supports for community participation, daily activities and supported independent living.

Authentic
Likeminded people wanting to make a difference in participant's lives.

Our aim to provide holistic and empowering supports targeted towards creating independence and guidance for all participants and families.
Over 35 years of experience working with people that have psychosocial, intellectual, and cognitive disabilities.

Industry/Entity Type

disability and mental health

Contact Information for Business Card

logo - business name

Colors
0054AA
0677BA
7BADD7
CADEEF
E8F1F8
FFF300
FFF600
FEFA6F
FFFEC7
FFFEE8

Requirements
Must have
• want double sided business cards(wont let me change it)
Should not have
• any disability related pictures

```html
<!DOCTYPE html>
<html lang="en">
<head>
<meta charset="utf-8">
<title>Wrenfield Disability – Business Card</title>
<link href="https://fonts.googleapis.com/css2?family=Montserrat:wght@400;500;600;700&display=swap" rel="stylesheet">
<style>
  :root {
    --navy: #1c3d66;
    --navy-deep: #183a63;
    --gold: #f7b928;
    --sky: #7badd7;
    --white: #ffffff;
    --page: #eeeeee;
    --card-w: 540px;
    --card-h: 310px;
  }
  * { margin: 0; padding: 0; box-sizing: border-box; }
  html, body {
    width: 1200px;
    height: 1079px;
    overflow: hidden;
    background: var(--page);
    font-family: "Montserrat", sans-serif;
  }
  .sheet {
    width: 1200px;
    height: 1079px;
    display: flex;
    align-items: center;
    justify-content: center;
    gap: 44px;
  }
  .card {
    position: relative;
    width: var(--card-w);
    height: var(--card-h);
    background: var(--navy);
    box-shadow: 0 6px 14px rgba(0, 0, 0, 0.28);
    color: var(--white);
    overflow: hidden;
  }
  .card--front {
    background: linear-gradient(118deg, var(--navy-deep) 0%, var(--navy-deep) 42%, #4a5a55 68%, #b0922f 86%, var(--gold) 100%);
  }
  .brand {
    position: absolute;
    left: 44px;
    bottom: 52px;
    display: flex;
    align-items: center;
    gap: 10px;
  }
  .brand__dot {
    width: 16px;
    height: 16px;
    border: 1.5px solid var(--sky);
    border-radius: 50%;
    flex: none;
  }
  .brand__name {
    font-size: 13px;
    font-weight: 600;
    letter-spacing: 0.6px;
    text-transform: uppercase;
    color: var(--white);
    white-space: nowrap;
  }
  .identity {
    position: absolute;
    right: 28px;
    top: 146px;
    text-align: right;
    font-size: 18px;
    letter-spacing: 0.3px;
    white-space: nowrap;
  }
  .identity__role { font-weight: 400; }
  .identity__name { font-weight: 700; font-size: 22px; }
  .rule {
    position: absolute;
    left: 38px;
    right: 28px;
    top: 180px;
    height: 3px;
    background: linear-gradient(90deg, var(--sky) 0%, #a9b8a0 40%, var(--gold) 100%);
  }
  .contacts {
    position: absolute;
    left: 38px;
    top: 200px;
    list-style: none;
    font-size: 12px;
    line-height: 1.55;
    white-space: nowrap;
  }
  .contacts b { font-weight: 700; display: inline-block; width: 18px; }
</style>
</head>
<body>
  <main class="sheet">
    <section class="card card--front" aria-label="Card front">
      <div class="brand">
        <span class="brand__dot"></span>
        <span class="brand__name">Wrenfield Disability</span>
      </div>
    </section>
    <section class="card card--back" aria-label="Card back">
      <p class="identity"><span class="identity__role">FOUNDER / </span><span class="identity__name">JOHN DOE</span></p>
      <div class="rule"></div>
      <ul class="contacts">
        <li><b>P :</b> +00 000 000 000</li>
        <li><b>E :</b> hello@wrenfieldcare.org</li>
        <li><b>W:</b> www.wrenfieldcare.org</li>
      </ul>
    </section>
  </main>
</body>
</html>
```